Chicago Train Advertisement for HomeAlongRail.com.

We have purchased one month of advertising on the Chicago NRX subway train. We will have 150 cards up in the subway to advertise our website HomeAlongRail.com where people can search for properties by train station. The cards are 11" tall and 46.5" long. We want people to feel compelled to jump on their cell phones and conduct a search for an apartment or home while they are riding the train, or at least enter their email and search criteria so one of our agents can help them.

Target Market(s)

People who want to live near train stations

Industry/Entity Type

Real Estate

Font styles to use
Sans Serif

Colors

Designer to choose colors to be used in the design.

Requirements
Must have
• The homealongrail logo and a catchy slogan, something like: Find your home near a train station the easy way: www.homealongrail.com. Search real estate listings near the NRX or Vorlo.

```html
<!DOCTYPE html>
<html lang="en">
<head>
<meta charset="utf-8">
<title>HomeAlongRail.com – Train Card</title>
<link href="https://fonts.googleapis.com/css2?family=Montserrat:wght@400;500;600&display=swap" rel="stylesheet">
<style>
  :root {
    --backdrop: #e9eaec;
    --card: #ffffff;
    --navy: #1b2140;
    --brand-blue: #1d8fd6;
    --muted: #55596a;
    --rail-yellow: #f2e400;
    --sky-top: #2c64c9;
    --sky-low: #6f95d6;
    --house-tone: #b58f92;
    --garden: #4c7a34;
  }
  * { margin: 0; padding: 0; box-sizing: border-box; }
  html, body {
    width: 1200px; height: 636px; overflow: hidden;
    background: var(--backdrop);
    font-family: "Montserrat", Arial, sans-serif;
  }
  .train-card {
    position: absolute; left: 0; top: 176px;
    width: 1200px; height: 284px;
    background: var(--card);
    overflow: hidden;
  }
  .card-art { position: absolute; inset: 0; }
  .brand {
    position: absolute; left: 82px; top: 52px;
    display: flex; align-items: center; gap: 8px;
    color: var(--navy); font-size: 22px; font-weight: 500;
    letter-spacing: -0.3px;
  }
  .brand-dot {
    width: 16px; height: 16px; border-radius: 50%;
    background: var(--brand-blue);
  }
  .tagline {
    position: absolute; left: 108px; top: 110px;
    color: var(--brand-blue); font-size: 19px; font-weight: 500;
    line-height: 1.2;
  }
  .web-address {
    position: absolute; left: 130px; top: 168px;
    color: var(--navy); font-size: 37px; font-weight: 500;
    letter-spacing: -0.2px;
  }
  .search-note {
    position: absolute; left: 140px; top: 218px;
    color: var(--muted); font-size: 15px; font-weight: 400;
  }
  .partner {
    position: absolute; left: 545px; top: 158px;
    display: flex; align-items: center; gap: 6px;
    color: var(--brand-blue); font-size: 16px; font-weight: 500;
  }
  .partner-dot {
    width: 12px; height: 12px; border-radius: 50%;
    background: var(--brand-blue);
  }
</style>
</head>
<body>
  <section class="train-card">
    <svg class="card-art" width="1200" height="284" viewBox="0 0 1200 284">
      <defs>
        <linearGradient id="street-scene" x1="0" y1="0" x2="0" y2="1">
          <stop offset="0" stop-color="var(--sky-top)"/>
          <stop offset="0.45" stop-color="var(--sky-low)"/>
          <stop offset="0.8" stop-color="var(--house-tone)"/>
          <stop offset="1" stop-color="var(--garden)"/>
        </linearGradient>
      </defs>
      <path class="rail-stripe" fill="var(--rail-yellow)"
            d="M300 0 L380 0 Q760 150 1200 284 L1200 284 L1110 284 Q700 170 300 0 Z"/>
      <path class="rail-stripe" fill="var(--rail-yellow)"
            d="M400 0 L460 0 Q820 150 1200 250 L1200 268 Q780 180 400 0 Z"/>
      <path class="street-photo" role="img"
            aria-label="Photo of a row of painted Victorian houses under a blue sky"
            fill="url(#street-scene)"
            d="M470 0 L1200 0 L1200 240 Q820 150 470 0 Z"/>
    </svg>

    <div class="brand"><span class="brand-dot"></span>HomeAlongRail.com</div>
    <p class="tagline">Find your home near a<br>Train station the easy way</p>
    <p class="web-address">www.homealongrail.com</p>
    <p class="search-note">Search real estate listings near the NRX or Vorlo.</p>
    <div class="partner"><span class="partner-dot"></span>Wrenfield Realty</div>
  </section>
</body>
</html>
```